Stationery for Smart Solutions Company

We need a full stationery design for a startup company named: Vandrel Smart Solutions. We are a hi-tech company specialized in smart solutions for condominiums, buldings, airports, etc. We provide a full service solution for fiber optics connectivity, perimeter protection, A.I. surveillance cameras, internet of things, sensors, etc.

Our Stationery should have at least / minimum:
- Envelope
- Business Card
- Letterhead
- Cars
- Laneyards
- Badge
- Gifts
- Uniforms

Target Market(s)

Construction, Condominiums, Corporate, Industries

Colors
59FF00
82FF00
B8FF75
E3FFCB
F4FFEA

Requirements
Must have
• a very modern, corporate and hi-tech touch
Nice to have
• Vandrel is a disruptive company, so you should think outside-the-box and innovate, user your creativity and surprise us.

```html
<!DOCTYPE html>
<html lang="en">
<head>
<meta charset="utf-8">
<title>Vandrel Staff ID Card</title>
<link rel="stylesheet" href="https://fonts.googleapis.com/css2?family=Montserrat+Alternates:wght@400;600;700&family=Open+Sans:wght@400&display=swap">
<style>
  :root {
    --backdrop: #d8d8d8;
    --card: #52555a;
    --card-pattern: #5b5e63;
    --accent: #9dfc23;
    --text-light: #ececec;
    --white: #ffffff;
    --photo: #a6a6a6;
  }
  * { margin: 0; padding: 0; box-sizing: border-box; }
  html, body { width: 1009px; height: 1200px; overflow: hidden; }
  body {
    background: var(--backdrop);
    position: relative;
    font-family: "Montserrat Alternates", sans-serif;
  }
  .card {
    position: absolute;
    left: 158px;
    width: 687px;
    height: 448px;
    background: var(--card);
    overflow: hidden;
  }
  .card-front { top: 143px; }
  .card-back { top: 615px; height: 444px; }

  .brand-name {
    position: absolute;
    left: 0; right: 0;
    top: 30px;
    text-align: center;
    font-weight: 700;
    font-size: 62px;
    line-height: 1;
    color: var(--white);
    letter-spacing: -1px;
  }
  .card-title {
    position: absolute;
    left: 0; right: 0;
    top: 128px;
    text-align: center;
    font-weight: 600;
    font-size: 30px;
    color: var(--accent);
  }
  .photo-slot {
    position: absolute;
    left: 164px;
    top: 202px;
    width: 134px;
    height: 166px;
    border-radius: 12px;
    background: var(--photo);
  }
  .holder-fields {
    position: absolute;
    left: 357px;
    top: 190px;
    list-style: none;
    font-size: 22px;
    line-height: 30.5px;
    color: var(--text-light);
  }
  .signature {
    position: absolute;
    top: 398px;
    font-family: "Open Sans", sans-serif;
    font-size: 16px;
    color: var(--white);
  }
  .signature-holder { left: 46px; }
  .signature-authorised { right: 65px; }
  .accent-band {
    position: absolute;
    left: 0; right: 0;
    bottom: 0;
    height: 16px;
    background: var(--accent);
  }

  .back-texture {
    position: absolute;
    inset: 0;
    background: linear-gradient(180deg, var(--card-pattern), var(--card));
  }
  .back-brand {
    position: absolute;
    left: 0; right: 0;
    top: 222px;
    display: flex;
    justify-content: center;
    align-items: center;
    gap: 10px;
  }
  .back-brand-dot {
    width: 22px; height: 22px;
    border-radius: 50%;
    background: var(--accent);
  }
  .back-brand-name {
    font-weight: 700;
    font-size: 32px;
    color: var(--white);
  }
  .contact {
    position: absolute;
    left: 0; right: 0;
    text-align: center;
    font-size: 18px;
    line-height: 22px;
    color: var(--white);
  }
  .contact-address { top: 290px; }
  .contact-reach { top: 356px; }
</style>
</head>
<body>
  <section class="card card-front">
    <div class="brand-name">Vandrel</div>
    <div class="card-title">Staff .I.D. CARD</div>
    <div class="photo-slot" role="img" aria-label="Staff member photo placeholder"></div>
    <ul class="holder-fields">
      <li>Your Name</li>
      <li>Position</li>
      <li>Date of birth</li>
      <li>Sex</li>
      <li>Blood group</li>
      <li>Valid up to :</li>
    </ul>
    <div class="signature signature-holder">Card holder signature</div>
    <div class="signature signature-authorised">Authorised signature</div>
    <div class="accent-band"></div>
  </section>

  <section class="card card-back">
    <div class="back-texture" role="img" aria-label="Repeating embossed brand pattern background"></div>
    <div class="back-brand">
      <span class="back-brand-dot"></span>
      <span class="back-brand-name">Vandrel</span>
    </div>
    <p class="contact contact-address">412 Cedarbrook Way<br>Fairview, Oregon 97024</p>
    <p class="contact contact-reach">555-014-2290 | info@vandrel.com<br>www.Vandrel.com</p>
  </section>
</body>
</html>
```